Landscape and Lawn Service start up company looking for an exciting and original flyer design.

We are looking for an exciting original flyer to promote our new Landscape and lawn care business. Services that we provide are full service lawn mowing including trimming and edging. We also offer bush and hedge trimming,. Fall and Spring yard cleanup, Leaf removal, Landscape bed rejuvenation and maintenance, New bed installs, mulching and gutter clean outs. we also offer pressure washing.

Will the flyer be editable? Ive included our logo file.

Lawn Care

```html
<!DOCTYPE html>
<html lang="en">
<head>
<meta charset="utf-8">
<title>Greenmoor Yard &amp; Lawn Flyer</title>
<link href="https://fonts.googleapis.com/css2?family=Oswald:wght@400;600;700&family=Open+Sans:ital,wght@0,600;0,700;1,700&display=swap" rel="stylesheet">
<style>
:root{
  --green-deep:#0c3a0e;
  --green-dark:#15561a;
  --green-mid:#2f8124;
  --green-light:#9fd23a;
  --yellow:#f5e33a;
  --note:#f7e04a;
  --white:#ffffff;
  --ink:#1b1b1b;
}
*{margin:0;padding:0;box-sizing:border-box}
html,body{width:898px;height:1200px;overflow:hidden;background:var(--white)}
.flyer{position:relative;width:898px;height:1200px;overflow:hidden;
  background:radial-gradient(ellipse at 45% 45%,var(--green-mid) 0%,var(--green-dark) 60%,var(--green-deep) 100%);
  font-family:'Open Sans',sans-serif;color:var(--white)}
.brand{position:absolute;left:50px;top:36px}
.brand-name{font-family:'Oswald',sans-serif;font-weight:700;font-size:104px;line-height:1;color:var(--green-light);letter-spacing:4px}
.brand-sub{font-family:'Oswald',sans-serif;font-weight:400;font-size:26px;letter-spacing:1px;margin-top:4px;white-space:nowrap}
.tagline{font-family:'Oswald',sans-serif;font-size:24px;color:var(--green-light);margin-top:2px;white-space:nowrap}
.credentials{position:absolute;left:600px;top:36px;list-style:none}
.credentials li{display:flex;align-items:center;gap:12px;font-weight:700;font-style:italic;font-size:26px;line-height:38px;white-space:nowrap}
.credentials svg{width:24px;height:24px}
.photo{position:absolute;border:9px solid var(--white);box-shadow:0 6px 16px rgba(0,0,0,.45)}
.photo-garden{left:48px;top:250px;width:450px;height:360px;transform:rotate(-5deg);
  background:linear-gradient(170deg,#6f9a48 0%,#8aa85a 35%,#3f7a2a 60%,#5e9a35 100%)}
.photo-yard{left:470px;top:228px;width:370px;height:270px;transform:rotate(6deg);
  background:linear-gradient(180deg,#31572a 0%,#5a8a3a 45%,#a6c85a 75%,#6fa33f 100%)}
.photo-house{left:475px;top:460px;width:385px;height:260px;transform:rotate(-3deg);
  background:linear-gradient(180deg,#d9dcc8 0%,#a7b08a 35%,#c9577e 55%,#3f9a2e 75%,#56b33a 100%)}
.headline{position:absolute;left:60px;top:640px;font-family:'Oswald',sans-serif;font-weight:700;font-size:72px;line-height:1.1;color:var(--yellow);letter-spacing:1px;white-space:nowrap}
.services{position:absolute;left:66px;top:752px;display:grid;grid-template-columns:270px 250px;column-gap:10px}
.services ul{list-style:none}
.services li{font-family:'Oswald',sans-serif;font-weight:400;font-size:24px;line-height:42px;white-space:nowrap}
.services li::before{content:"•";margin-right:10px}
.area-note{position:absolute;left:640px;top:770px;width:225px;height:140px;background:var(--note);
  transform:rotate(-18deg);box-shadow:0 6px 12px rgba(0,0,0,.4);color:var(--ink);
  font-weight:700;font-style:italic;font-size:20px;line-height:28px;padding:14px 12px;text-align:center}
.price{position:absolute;left:60px;top:992px;font-weight:700;font-style:italic;font-size:30px;color:var(--yellow);white-space:nowrap}
.payment{position:absolute;right:48px;top:968px}
.payment-label{font-weight:700;font-style:italic;font-size:20px}
.payment-cards{display:flex;gap:8px;margin-top:6px}
.payment-cards span{width:50px;height:32px;border-radius:4px;background:var(--white)}
.contact-band{position:absolute;left:0;top:1052px;width:898px;height:148px;background:var(--green-deep)}
.address{position:absolute;left:60px;top:30px;font-weight:700;font-size:32px;line-height:44px;white-space:nowrap}
.call{position:absolute;left:470px;top:24px}
.call-label{font-weight:700;font-size:19px;color:var(--yellow);letter-spacing:.5px;white-space:nowrap}
.phone{font-family:'Oswald',sans-serif;font-weight:600;font-size:62px;line-height:1.2;letter-spacing:2px;white-space:nowrap}
</style>
</head>
<body>
<div class="flyer">
  <header class="brand">
    <div class="brand-name">GMYL</div>
    <div class="brand-sub">GREENMOOR YARD &amp; LAWN</div>
    <div class="tagline">Specialist for your environment</div>
  </header>

  <ul class="credentials">
    <li><svg viewBox="0 0 24 24"><path d="M3 13l6 6L21 5" fill="none" stroke="#f5e33a" stroke-width="4"/></svg>Residential</li>
    <li><svg viewBox="0 0 24 24"><path d="M3 13l6 6L21 5" fill="none" stroke="#f5e33a" stroke-width="4"/></svg>Commercial</li>
    <li><svg viewBox="0 0 24 24"><path d="M3 13l6 6L21 5" fill="none" stroke="#f5e33a" stroke-width="4"/></svg>Licenced</li>
    <li><svg viewBox="0 0 24 24"><path d="M3 13l6 6L21 5" fill="none" stroke="#f5e33a" stroke-width="4"/></svg>Fully Insured</li>
  </ul>

  <div class="photo photo-garden" role="img" aria-label="Landscaped garden with lawn, stone steps and flower beds"></div>
  <div class="photo photo-yard" role="img" aria-label="Green yard with trees and shrubs"></div>
  <div class="photo photo-house" role="img" aria-label="House with trimmed lawn and pink flower beds"></div>

  <h1 class="headline">WE DO IT ALL</h1>

  <div class="services">
    <ul>
      <li>Lawn Mowing</li>
      <li>Trimming</li>
      <li>Bush and Hedge Trimming</li>
      <li>Fall &amp; Spring Yard Cleanup</li>
      <li>Leaf removal</li>
    </ul>
    <ul>
      <li>Mulching</li>
      <li>Gutter Clean Outs</li>
      <li>Pressure washing</li>
      <li>Landscape Bed Rejuvenation</li>
      <li>New Bed Installs</li>
    </ul>
  </div>

  <div class="area-note">Service areas are Ridgefield, Oakvale, Marlow City and Fernbrook</div>

  <p class="price">Lawn care as low as $18 Weekly</p>

  <div class="payment">
    <div class="payment-label">We Accept</div>
    <div class="payment-cards"><span></span><span></span><span></span><span></span></div>
  </div>

  <footer class="contact-band">
    <div class="address">418 North Elm Avenue<br>Brookhaven, IL 62950</div>
    <div class="call">
      <div class="call-label">CALL US TODAY FOR FREE ESTIMATE</div>
      <div class="phone">555 210 4873</div>
    </div>
  </footer>
</div>
</body>
</html>
```